Photo/Video Company needs a business card design

We need a business card design for a photo/video production company called 'Corvane Studio'. We primarily do wedding photography and videography, however we also do commercial, corporate, and promo work.

We would like a clean, white design that primarily markets us as a wedding photo/video company, but still sleek enough that we attract corporate and commercial clients.

Industry/Entity Type

Wedding

Requirements
Must have
• We wish the front of the business card to simply have the logo, and the back will have the contact information:

Corvane Studio
Wedding, Event, Corporate, Commercial, Promo
647-518-2063
info@corvanestudio.example
www.corvanestudio.example

We are hoping for a version of the card that has only the companies name on it, as well as several variations that have different employees names printed.

The employee names and titles are:

Tom Belliwe - Photo/Video
Deklan Belliwe - Photo/Video
Pieter Walcox -Video
Lydia Prohane -Photo/Video

The design should use similar fonts in the writing as the fonts used in the logo design. The AI file will be provided.
Nice to have
• We also might like to see the front of the card have the main logo, as well as 'Wedding, Event, Corporate, Commercial, Promo' written in the bottom corner.
Should not have
• No old style fonts should be used. Also no other graphic images should be created, but we are open to the possibility of having shapes and borders.

```html
<!DOCTYPE html>
<html lang="en">
<head>
<meta charset="utf-8">
<title>Corvane Studio — Business Card</title>
<link rel="stylesheet" href="https://fonts.googleapis.com/css2?family=Michroma&family=Montserrat:wght@400;500&display=swap">
<style>
  :root {
    --backdrop: #c6c6c6;
    --card: #ffffff;
    --ink: #2b2b2b;
    --ink-soft: #555555;
    --band: #0a0a0a;
    --band-text: #ffffff;
    --accent: #b3161d;
  }
  * { margin: 0; padding: 0; box-sizing: border-box; }
  html, body {
    width: 1200px; height: 765px; overflow: hidden;
    background: var(--backdrop);
  }
  .sheet { position: relative; width: 1200px; height: 765px; }

  .card {
    position: absolute; top: 302px;
    width: 575px; height: 344px;
    border-radius: 44px;
    background: linear-gradient(180deg, #fbfbfb 0%, var(--card) 45%, #f4f4f4 100%);
    overflow: hidden;
  }
  .card--front { left: 16px; }
  .card--back  { left: 604px; }

  /* Front */
  .brand {
    position: absolute; left: 0; right: 0; top: 132px;
    display: flex; align-items: center; justify-content: center; gap: 16px;
  }
  .brand__mark { width: 22px; height: 22px; background: var(--accent); }
  .brand__name {
    font-family: "Michroma", sans-serif; font-size: 30px;
    color: var(--ink-soft); text-transform: uppercase; letter-spacing: 0.5px;
  }
  .services {
    font-family: "Montserrat", sans-serif; font-weight: 400;
    text-transform: uppercase; white-space: nowrap;
  }
  .services--front {
    position: absolute; left: 46px; top: 285px;
    font-size: 12px; letter-spacing: 2.6px; color: var(--ink);
  }
  .services .sep { margin: 0 8px; }

  /* Back */
  .person { position: absolute; left: 257px; top: 86px; }
  .person__name {
    font-family: "Michroma", sans-serif; font-size: 23px;
    color: var(--ink); text-transform: uppercase; line-height: 1;
  }
  .person__role {
    margin: 9px 0 0 7px;
    font-family: "Michroma", sans-serif; font-size: 12px;
    letter-spacing: 2px; color: var(--ink);
  }
  .band {
    position: absolute; left: 0; right: 0; top: 144px; height: 31px;
    background: var(--band);
    box-shadow: 0 4px 5px rgba(0,0,0,0.18);
    display: flex; align-items: center; padding-left: 43px;
  }
  .services--band {
    font-size: 14px; font-weight: 500; letter-spacing: 0.6px; color: var(--band-text);
  }
  .services--band .sep { margin: 0 7px; }

  .contacts {
    position: absolute; left: 235px; top: 203px;
    list-style: none;
  }
  .contacts__item {
    display: flex; align-items: center; height: 26px;
  }
  .contacts__icon { width: 22px; height: 22px; flex: none; }
  .contacts__text {
    margin-left: 17px;
    font-family: "Michroma", sans-serif; font-size: 13px; color: var(--ink);
    white-space: nowrap;
  }
</style>
</head>
<body>
<div class="sheet">

  <section class="card card--front" aria-label="Card front">
    <div class="brand">
      <span class="brand__mark"></span>
      <span class="brand__name">Corvane Studio</span>
    </div>
    <p class="services services--front">
      Wedding<span class="sep">|</span>Event<span class="sep">|</span>Corporate<span class="sep">|</span>Commercial<span class="sep">|</span>Promo
    </p>
  </section>

  <section class="card card--back" aria-label="Card back">
    <div class="person">
      <p class="person__name">Tom Belliwe</p>
      <p class="person__role">Photo/Video</p>
    </div>

    <div class="band">
      <p class="services services--band">
        Wedding<span class="sep">|</span>Event<span class="sep">|</span>Corporate<span class="sep">|</span>Commercial<span class="sep">|</span>Promo
      </p>
    </div>

    <ul class="contacts">
      <li class="contacts__item">
        <svg class="contacts__icon" viewBox="0 0 22 22" aria-hidden="true">
          <rect width="22" height="22" rx="4" fill="#111"/>
          <path d="M5 9.5c0-2 2.7-3 6-3s6 1 6 3l-1 .8-2.2-.6V8.6c-1.8-.6-3.8-.6-5.6 0v1.1L6 10.3z" fill="#fff"/>
          <rect x="6.5" y="11" width="9" height="5" rx="1" fill="#fff"/>
          <circle cx="11" cy="13.5" r="1.3" fill="#111"/>
        </svg>
        <span class="contacts__text">647-518-2063</span>
      </li>
      <li class="contacts__item">
        <svg class="contacts__icon" viewBox="0 0 22 22" aria-hidden="true">
          <rect width="22" height="22" rx="4" fill="#111"/>
          <rect x="5" y="7" width="12" height="9" rx="1" fill="#fff"/>
          <path d="M5.5 7.5 11 12l5.5-4.5" fill="none" stroke="#111" stroke-width="1.2"/>
        </svg>
        <span class="contacts__text">info@corvanestudio.example</span>
      </li>
      <li class="contacts__item">
        <svg class="contacts__icon" viewBox="0 0 22 22" aria-hidden="true">
          <rect width="22" height="22" rx="4" fill="#111"/>
          <g fill="none" stroke="#fff" stroke-width="1.1">
            <circle cx="11" cy="11" r="6"/>
            <ellipse cx="11" cy="11" rx="2.6" ry="6"/>
            <path d="M5 11h12M6 8h10M6 14h10"/>
          </g>
        </svg>
        <span class="contacts__text">www.corvanestudio.example</span>
      </li>
    </ul>
  </section>

</div>
</body>
</html>
```